Business Card for Bloom Vitality & Strength

Hi can you please design a business card with my logo and program logo (the new one I just sent) somewhere on it too maybe on the back? Needs to be eye catching and super cool.
Trudy Melcombe, Director
Master Personal Trainer & Nutrition Coach
0472 816 305
Www.bloomvitalitystrength.com.au
Insta (logo) bloom_vitality_strength #bloomyou7x72018

Target Market(s)

30+ women looking to change lifestyle to healthy mind body etc

Industry/Entity Type

Health And Wellness

Contact Information for Business Card

As above

Font styles to use
Sans Serif

Colors

Designer to choose colors to be used in the design.

Requirements
Must have
• Must super cool and edgy with a bit of cuteness

```html
<!DOCTYPE html>
<html lang="en">
<head>
<meta charset="utf-8">
<title>Bloom Vitality &amp; Strength – Business Card</title>
<link rel="stylesheet" href="https://fonts.googleapis.com/css2?family=Roboto:wght@400;700&family=Roboto+Condensed:wght@500&display=swap">
<style>
  :root {
    --backdrop: #b9b9b9;
    --red-bright: #cf0a0a;
    --red-deep: #8a0000;
    --red-name: #8e0f0f;
    --ink: #141414;
    --ink-soft: #2a2a2a;
    --paper: #f1f1f1;
    --white: #ffffff;
  }
  * { box-sizing: border-box; margin: 0; padding: 0; }
  html, body {
    width: 1200px; height: 576px; overflow: hidden;
    background: var(--backdrop);
    font-family: "Roboto", Arial, sans-serif;
  }
  .stage { position: relative; width: 1200px; height: 576px; }

  .card {
    position: absolute; top: 138px;
    width: 484px; height: 294px;
    border-radius: 16px; overflow: hidden;
  }

  /* Front */
  .card-front {
    left: 82px;
    background: radial-gradient(ellipse at 45% 40%, var(--red-bright) 0%, #b30404 50%, var(--red-deep) 100%);
  }
  .front-brand {
    position: absolute; left: 84px; top: 118px; width: 320px;
    color: var(--ink); font-weight: 700; text-transform: uppercase;
  }
  .front-brand .brand-line-1 { font-size: 37px; line-height: 1; letter-spacing: 0.5px; white-space: nowrap; }
  .front-brand .brand-line-2 { font-size: 17px; line-height: 1; margin-top: 14px; letter-spacing: 12.5px; white-space: nowrap; }
  .front-dot {
    position: absolute; left: 52px; top: 124px;
    width: 22px; height: 22px; border-radius: 50%; background: var(--white);
  }

  /* Back */
  .card-back { left: 602px; background: var(--paper); }
  .back-accent {
    position: absolute; left: 232px; top: -10px;
    width: 320px; height: 320px; border-radius: 50%;
    background: radial-gradient(circle at 70% 40%, #e00d0d 0%, #b50505 45%, var(--red-deep) 100%);
  }
  .back-brand {
    position: absolute; left: 22px; top: 50px;
    color: var(--ink); font-weight: 700; text-transform: uppercase;
  }
  .back-brand .brand-line-1 { font-size: 21px; line-height: 1; white-space: nowrap; }
  .back-brand .brand-line-2 { font-size: 10px; line-height: 1; margin-top: 8px; letter-spacing: 7.4px; white-space: nowrap; }
  .back-dot {
    position: absolute; left: 118px; top: 52px;
    width: 46px; height: 46px; border-radius: 50%; background: #b80606; z-index: 0;
  }
  .back-brand { z-index: 1; }

  .person { position: absolute; left: 22px; top: 144px; }
  .person-name {
    font-family: "Roboto Condensed", "Arial Narrow", sans-serif;
    font-weight: 500; font-size: 20px; color: var(--red-name); line-height: 1;
  }
  .person-role { margin-top: 8px; font-size: 12px; line-height: 15px; color: var(--ink-soft); }

  .contact-list { position: absolute; left: 24px; top: 207px; list-style: none; }
  .contact-list li {
    display: flex; align-items: center; gap: 8px;
    height: 18px; font-size: 12px; color: var(--ink-soft);
  }
  .contact-icon { width: 10px; height: 10px; flex: none; }
  .contact-square { width: 9px; height: 9px; flex: none; background: var(--red-name); border-radius: 2px; }

  .program-mark {
    position: absolute; left: 346px; top: 236px; width: 116px;
    border-top: 1px solid var(--ink); border-bottom: 1px solid var(--ink);
    padding: 3px 0; text-align: center;
    font-size: 14px; font-weight: 400; color: var(--ink); letter-spacing: 0.5px;
  }
</style>
</head>
<body>
<main class="stage">

  <section class="card card-front" aria-label="Card front">
    <span class="front-dot"></span>
    <div class="front-brand">
      <div class="brand-line-1">Bloom Vitality</div>
      <div class="brand-line-2">&amp; Strength</div>
    </div>
  </section>

  <section class="card card-back" aria-label="Card back">
    <div class="back-accent"></div>

    <span class="back-dot"></span>
    <div class="back-brand">
      <div class="brand-line-1">Bloom Vitality</div>
      <div class="brand-line-2">&amp; Strength</div>
    </div>

    <div class="person">
      <h1 class="person-name">Trudy Melcombe, Director</h1>
      <p class="person-role">Master Personal Trainer<br>&amp; Nutrition Coach</p>
    </div>

    <ul class="contact-list">
      <li>
        <svg class="contact-icon" viewBox="0 0 10 10" aria-hidden="true"><path fill="#8e0f0f" d="M1 3.2C1 2 2.5 1 5 1s4 1 4 2.2L7.4 4 6.8 3H3.2l-.6 1zM2.5 5h5l1 4h-7z"/></svg>
        0472 816 305
      </li>
      <li>
        <svg class="contact-icon" viewBox="0 0 10 10" aria-hidden="true"><rect x="0.5" y="2" width="9" height="6.5" fill="#8e0f0f"/><path d="M0.8 2.3 5 5.6 9.2 2.3" fill="none" stroke="#f1f1f1" stroke-width="0.9"/></svg>
        trudy@bloomvitalitystrength.com.au
      </li>
      <li>
        <svg class="contact-icon" viewBox="0 0 10 10" aria-hidden="true"><g fill="none" stroke="#8e0f0f" stroke-width="1"><circle cx="5" cy="5" r="4.3"/><ellipse cx="5" cy="5" rx="1.8" ry="4.3"/><path d="M0.7 5h8.6M1.4 2.8h7.2M1.4 7.2h7.2"/></g></svg>
        www.bloomvitalitystrength.com.au
      </li>
      <li>
        <span class="contact-square"></span>
        #bloom_vitality_strength, #bloomyou7x72018
      </li>
    </ul>

    <div class="program-mark">BloomYou7x7</div>
  </section>

</main>
</body>
</html>
```